New Dog Treat Business Needs Promotional Flyer

We need a flyer designed for a new dog treat company to launch our business at an upcoming industry trade show that also is open to the public.

The design should project a healthy aspect and if possible say some of the things that are in our sliding banners on our website.

We would like to see designs that include our logo and make reference to our website which is
www.tilbysbakehouse.com.au

We hope to use the flyer for other promotions and therefore would prefer that there is no information that would make the flyer outdated quickly.

Target Market(s)

Dog Lovers who want fresh healthy treats that contain only human grade ingredients.

Industry/Entity Type

Industry

Font styles to use
Serif

Requirements
Must have
• Include our log or at least part of our logo and reference to our website.
Nice to have
• Something creative and unique
Should not have
• Anything that dates the flyer as we want to use this again in the future.

```html
<!DOCTYPE html>
<html lang="en">
<head>
<meta charset="utf-8">
<title>Tilby's Bakehouse – Healthy Dog Treats Flyer</title>
<link rel="stylesheet" href="https://fonts.googleapis.com/css2?family=Arimo:wght@400;700&display=swap">
<style>
  :root {
    --paper: #ead7b6;
    --paper-stripe: #e2cda8;
    --cocoa: #2e1a10;
    --cocoa-mid: #4a2c1a;
    --cream-edge: #f7eedd;
    --cherry: #d4161c;
    --ink: #4a3b30;
    --white: #ffffff;
    --frame: #f4f1ec;
    --mark: #555555;
  }
  * { margin: 0; padding: 0; box-sizing: border-box; }
  html, body { width: 1200px; height: 2265px; overflow: hidden; background: var(--paper); }
  .flyer {
    position: relative;
    width: 1200px;
    height: 2265px;
    overflow: hidden;
    font-family: "Arimo", Arial, sans-serif;
    background:
      repeating-linear-gradient(0deg, var(--paper) 0 14px, var(--paper-stripe) 14px 16px),
      var(--paper);
  }
  .flyer::after {
    content: "";
    position: absolute; inset: 0;
    background: radial-gradient(ellipse at 30% 55%, rgba(255,250,240,.45), rgba(255,250,240,0) 70%);
    pointer-events: none;
  }
  .header-wave { position: absolute; left: 0; top: 0; width: 1200px; height: 200px; z-index: 1; }
  .crop-marks { position: absolute; inset: 0; width: 1200px; height: 2265px; z-index: 5; pointer-events: none; }

  .dogs-photo {
    position: absolute; left: 488px; top: 170px; width: 620px; height: 650px;
    background: linear-gradient(160deg, #f6f2ec 0%, #d9b98e 40%, #6b4a30 65%, #efe8de 100%);
    z-index: 2;
  }
  .promise-pill {
    position: absolute; left: 131px; top: 307px; width: 380px; height: 625px;
    background: var(--cherry);
    border: 6px solid var(--white);
    border-radius: 70px;
    box-shadow: 0 6px 14px rgba(60,30,10,.35);
    color: var(--white);
    font-weight: 700;
    font-size: 37px;
    line-height: 46px;
    text-align: center;
    display: flex; align-items: center; justify-content: center;
    padding: 16px 10px;
    z-index: 3;
  }

  .treat-gallery {
    position: absolute; left: 630px; top: 806px; width: 390px; height: 940px;
    background: var(--frame);
    padding: 12px;
    display: flex; flex-direction: column; gap: 14px;
    z-index: 2;
  }
  .treat-photo { flex: 1; border-radius: 18px; }
  .treat-photo--biscuits { background: linear-gradient(135deg, #e8d2ae, #c9a06c 55%, #e4caa0); }
  .treat-photo--cookies { background: linear-gradient(135deg, #cdb08a, #9c7550 55%, #d8bd96); }
  .treat-photo--rounds { background: linear-gradient(135deg, #c96a2a, #8a3d16 55%, #d98a3e); }

  .story {
    position: absolute; left: 131px; top: 955px; width: 470px;
    color: var(--ink);
    font-size: 29px;
    line-height: 38px;
    text-align: justify;
    z-index: 2;
  }
  .story p + p { margin-top: 38px; }

  .location-line {
    position: absolute; left: 131px; top: 1950px; width: 400px;
    color: var(--cherry);
    font-weight: 700;
    font-size: 40px;
    line-height: 48px;
    text-align: center;
    z-index: 2;
  }

  .brand {
    position: absolute; left: 656px; top: 1763px; width: 364px; height: 337px;
    background: var(--white);
    display: flex; flex-direction: column; align-items: center; justify-content: center;
    gap: 14px;
    z-index: 2;
  }
  .brand-dot { width: 56px; height: 56px; border-radius: 50%; background: var(--cherry); }
  .brand-name { font-weight: 700; font-size: 34px; color: var(--cocoa-mid); }
  .brand-site { font-size: 19px; color: var(--cocoa-mid); }
</style>
</head>
<body>
<main class="flyer">
  <svg class="header-wave" viewBox="0 0 1200 200" aria-hidden="true">
    <path d="M0 0 H1200 V170 C1000 140 720 95 470 95 C280 95 120 120 0 140 Z" fill="var(--cream-edge)"/>
    <path d="M0 0 H1200 V150 C1000 120 720 78 470 78 C280 78 120 100 0 120 Z" fill="var(--cocoa-mid)"/>
    <path d="M0 0 H1200 V132 C1000 105 720 65 470 65 C280 65 120 85 0 102 Z" fill="var(--cocoa)"/>
  </svg>

  <div class="dogs-photo" role="img" aria-label="Photo of four happy dogs sitting together on a white backdrop"></div>

  <div class="promise-pill">
    <p>All of our products comprise of human grade ingredients, as we firmly believe that you should not feed your dog anything that you are not willing to eat yourself.</p>
  </div>

  <div class="treat-gallery">
    <div class="treat-photo treat-photo--biscuits" role="img" aria-label="Photo of golden baked dog biscuits with a chalkboard label"></div>
    <div class="treat-photo treat-photo--cookies" role="img" aria-label="Photo of speckled baked dog cookies with a chalkboard label"></div>
    <div class="treat-photo treat-photo--rounds" role="img" aria-label="Photo of orange baked dog treat rounds with a chalkboard label"></div>
  </div>

  <section class="story">
    <p>Everything that we sell is handmade from the freshest farm produce. We use free range ingredients where available, and source the vast majority of our raw ingredients from Victorian farmers.</p>
    <p>All goods are baked on our premises and contain no added salt, sugar or preservatives. We believe in environmentally friendly practices with the majority of our packaging made from recycled paper.</p>
    <p>Our focus is on quality and not quantity, and therefore our production is limited to small batches, baked daily.</p>
  </section>

  <p class="location-line">Our dog bakery is located in the seaside suburb of Saltmarsh Bay.</p>

  <div class="brand">
    <span class="brand-dot" aria-hidden="true"></span>
    <span class="brand-name">Tilby's Bakehouse</span>
    <span class="brand-site">www.tilbysbakehouse.com.au</span>
  </div>

  <svg class="crop-marks" viewBox="0 0 1200 2265" aria-hidden="true">
    <g stroke="var(--mark)" stroke-width="2">
      <line x1="0" y1="45" x2="30" y2="45"/><line x1="45" y1="0" x2="45" y2="30"/>
      <line x1="1170" y1="45" x2="1200" y2="45"/><line x1="1155" y1="0" x2="1155" y2="30"/>
      <line x1="0" y1="2220" x2="30" y2="2220"/><line x1="45" y1="2235" x2="45" y2="2265"/>
      <line x1="1170" y1="2220" x2="1200" y2="2220"/><line x1="1155" y1="2235" x2="1155" y2="2265"/>
    </g>
  </svg>
</main>
</body>
</html>
```